Four different size banners for our website

Hello,

I need four different size banners for our website :

728px x 90px
300px x 250px
160px x 600px
468px x 68px

All animated gifs with 3 slides no bigger than 50kb.

We would like to advertise following headlines :

1 )CO2 System Aquarium Specialists

2) Free Worldwide Shipping, Free Returns & Free Setup Advice

3) Create your CO2 System. OUR STEP-BY-STEP GUIDE MAKES IT SIMPLE TO GET STARTED

Logo attached.

You can view our website here : www.fernvalelab.co.uk

```html
<!DOCTYPE html>
<html lang="en">
<head>
<meta charset="utf-8">
<title>Fernvale Lab – CO2 System Aquarium Specialists</title>
<link rel="stylesheet" href="https://fonts.googleapis.com/css2?family=Arimo:wght@400;700&family=Roboto+Condensed:wght@700&display=swap">
<style>
  :root {
    --bg: #ffffff;
    --ink: #1b1b1b;
    --brand-grey: #9a9a9a;
    --brand-grey-light: #c4c4c4;
    --green: #5fd81c;
    --green-light: #8cf24a;
    --white: #ffffff;
  }
  html, body {
    margin: 0;
    padding: 0;
    width: 1200px;
    height: 148px;
    overflow: hidden;
    background: var(--bg);
  }
  .banner {
    position: relative;
    width: 1200px;
    height: 148px;
    background: var(--bg);
    font-family: "Arimo", Arial, sans-serif;
    color: var(--ink);
  }
  .brand-badge {
    position: absolute;
    left: 13px;
    top: 29px;
    width: 90px;
    height: 90px;
    border-radius: 50%;
    background: var(--brand-grey-light);
    display: flex;
    align-items: center;
    justify-content: center;
    text-align: center;
  }
  .brand-badge__name {
    font-family: "Arimo", Arial, sans-serif;
    font-weight: 700;
    font-size: 15px;
    line-height: 1.1;
    color: var(--white);
  }
  .usp-row {
    position: absolute;
    left: 379px;
    top: 20px;
    right: 22px;
    display: flex;
    align-items: center;
    font-size: 16px;
    white-space: nowrap;
  }
  .usp-row__divider {
    width: 2px;
    height: 32px;
    background: var(--green);
    margin: 0 12px;
  }
  .cta {
    position: absolute;
    left: 376px;
    top: 71px;
    width: 280px;
    height: 28px;
    border-radius: 14px;
    background: linear-gradient(to bottom, var(--green-light), var(--green));
    color: var(--white);
    font-weight: 700;
    font-size: 14px;
    display: flex;
    align-items: center;
    justify-content: center;
    letter-spacing: 0.2px;
  }
  .cta-note {
    position: absolute;
    left: 377px;
    top: 109px;
    font-family: "Roboto Condensed", "Arial Narrow", sans-serif;
    font-weight: 700;
    font-size: 12.5px;
    text-transform: uppercase;
    white-space: nowrap;
  }
  .brand-wordmark {
    position: absolute;
    right: 22px;
    top: 88px;
    font-family: "Arimo", Arial, sans-serif;
    font-weight: 700;
    font-size: 30px;
    color: var(--brand-grey-light);
    white-space: nowrap;
  }
</style>
</head>
<body>
  <div class="banner">
    <div class="brand-badge">
      <span class="brand-badge__name">Fernvale<br>Lab</span>
    </div>

    <div class="usp-row">
      <span class="usp-row__item">CO2 System Aquarium Specialists</span>
      <span class="usp-row__divider"></span>
      <span class="usp-row__item">Free Worldwide Shipping</span>
      <span class="usp-row__divider"></span>
      <span class="usp-row__item">Free Returns &amp; Free Setup Advice</span>
    </div>

    <div class="cta">CREATE YOUR CO2 SYSTEM</div>
    <div class="cta-note">Our step-by-step guide makes it simple to get started</div>

    <div class="brand-wordmark">Fernvale Lab</div>
  </div>
</body>
</html>
```